Design our Hot Cup Jacket / Coffee Sleeve

I am looking for a chic and eye catchy design (using our logo) to put on our coffee cup sleeve to include our Cafe and our coffee truck. We do not need separate design. Both the Cafe and the coffee truck can be represented on the same Coffee Sleeve design. I have provided both logos; one for our Cafe which is called Marigold Cafe & Coffee Bar and the other logo is for our coffee truck which is called The Little Kettle. We would like a back and front design. Can you please include our instragram - marigoldcafeqrx and thelittlekettleqrx

Our Cafe serves breakfast and lunch consisting of full breakfast (pancakes, eggs, bacon, home fries, omeletts etc), lunch (made to order sandwiches and wraps, homemade soups, salads) and freshly baked scones, muffins, pies and cakes. I have also attached a few pictures of the Cafe food, outside on the deck of our Cafe and the Coffee Truck.

Target Market(s)

customers

Industry/Entity Type

Cafe, restaurant, coffee truck

Requirements
Must have
• logo, Instagram name, chic and classy, our logo color
Nice to have
• pictures

```html
<!DOCTYPE html>
<html lang="en">
<head>
<meta charset="utf-8">
<title>Coffee Sleeve – Option 1</title>
<link rel="stylesheet" href="https://fonts.googleapis.com/css2?family=Questrial&family=Fira+Sans+Condensed:wght@600&family=Crimson+Pro&display=swap">
<style>
  :root {
    --bg-top: #c4c4c4;
    --bg-bottom: #e6e6e6;
    --label: #111111;
    --sleeve: #f7f8fa;
    --rib: rgba(0, 0, 0, 0.04);
    --ink: #1c1c1c;
    --steel: #41728f;
    --steel-dark: #36627d;
    --pattern-light: #e3ebf1;
    --pattern-mid: #b9cdd9;
    --pattern-deep: #8fb0c3;
    --handle: #f1f4f6;
  }
  html, body {
    margin: 0;
    padding: 0;
    width: 1200px;
    height: 1200px;
    overflow: hidden;
  }
  body {
    position: relative;
    background: linear-gradient(180deg, var(--bg-top) 0%, var(--bg-bottom) 100%);
    font-family: "Questrial", sans-serif;
    color: var(--label);
  }
  .option-title {
    position: absolute;
    left: 44px;
    top: 36px;
    margin: 0;
    font-size: 38px;
    font-weight: 400;
    letter-spacing: 0.5px;
  }
  .side-label {
    position: absolute;
    top: 282px;
    margin: 0;
    font-size: 24px;
    font-weight: 400;
  }
  .side-label--one { left: 158px; }
  .side-label--two { left: 652px; }

  .sleeve {
    position: absolute;
    top: 515px;
    width: 360px;
    height: 300px;
    background:
      repeating-linear-gradient(90deg, transparent 0 3px, var(--rib) 3px 4px),
      var(--sleeve);
    clip-path: polygon(0 0, 100% 0, 96% 100%, 4% 100%);
  }
  .sleeve--cafe { left: 176px; }
  .sleeve--truck { left: 685px; }

  .brand {
    position: absolute;
    left: 0;
    right: 0;
    display: flex;
    align-items: center;
    justify-content: center;
    gap: 12px;
  }
  .brand--cafe { top: 62px; }
  .brand--truck { top: 52px; flex-direction: column; gap: 10px; }

  .brand-mark {
    flex: none;
    width: 40px;
    height: 40px;
    border-radius: 50%;
    background: var(--steel);
  }
  .brand--truck .brand-mark {
    width: 46px;
    height: 46px;
  }

  .brand-name {
    margin: 0;
    font-family: "Fira Sans Condensed", sans-serif;
    font-weight: 600;
    color: var(--ink);
    line-height: 1.05;
    text-align: left;
    font-size: 30px;
  }
  .brand--truck .brand-name {
    text-align: center;
    font-size: 30px;
  }

  .pattern-band {
    position: absolute;
    left: 0;
    right: 0;
    top: 160px;
    height: 90px;
    background:
      linear-gradient(90deg, var(--pattern-light) 0%, var(--pattern-mid) 22%, var(--pattern-deep) 50%, var(--pattern-mid) 78%, var(--pattern-light) 100%);
    opacity: 0.75;
  }

  .social-band {
    position: absolute;
    left: 0;
    right: 0;
    top: 252px;
    height: 30px;
    background: linear-gradient(180deg, var(--steel) 0%, var(--steel-dark) 100%);
    display: flex;
    align-items: center;
    justify-content: center;
    gap: 14px;
  }
  .handle {
    display: flex;
    align-items: center;
    gap: 5px;
    font-family: "Crimson Pro", serif;
    font-size: 12px;
    color: var(--handle);
  }
  .handle-dot {
    width: 11px;
    height: 11px;
    border-radius: 50%;
    background: var(--handle);
  }
</style>
</head>
<body>
  <h1 class="option-title">Option 1</h1>

  <p class="side-label side-label--one">Side1</p>
  <p class="side-label side-label--two">Side2</p>

  <section class="sleeve sleeve--cafe" aria-label="Cafe side of sleeve">
    <div class="brand brand--cafe">
      <span class="brand-mark"></span>
      <p class="brand-name">Marigold Cafe<br>&amp; Coffee Bar</p>
    </div>
    <div class="pattern-band" role="img" aria-label="Line-drawn band of coffee beans, cups, splashes and leaves"></div>
    <div class="social-band">
      <span class="handle"><span class="handle-dot"></span>marigoldcafeqrx</span>
      <span class="handle"><span class="handle-dot"></span>thelittlekettleqrx</span>
    </div>
  </section>

  <section class="sleeve sleeve--truck" aria-label="Coffee truck side of sleeve">
    <div class="brand brand--truck">
      <span class="brand-mark"></span>
      <p class="brand-name">The Little Kettle</p>
    </div>
    <div class="pattern-band" role="img" aria-label="Line-drawn band of coffee beans, cups, splashes and leaves"></div>
    <div class="social-band"></div>
  </section>
</body>
</html>
```